依頼詳細
●依頼内容
学部パンフレット(B5版で8ページの中綴じ冊子)の表紙デザインの作成をお願いします。
実際に依頼する方には、追加業務で表紙以外の7ページのデザインも依頼する予定です。写真、テキスト等のコンテンツを6/21までにお渡しし(p.2-3のイラストと一部のコンテンツは6月末)、7月10日頃に納品いただけますよう、お願い致します。
そのため、追加業務の見積金額もご提示いただけますようお願いします。

なお、パンフレットの内容は次の通りです。(添付資料もご参照ください。)
p.1表紙
p.2-3 見開きの全面イラスト(こちらで用意)+タイトル等
p.4-5 研究プロジェクト紹介(4学科、写真+本文)
p.6-7 卒業生の活躍紹介・就職情報
p.8 施設紹介、QRコード

●表紙デザインの作成について(添付資料もご覧ください。)
要素として、
・学部名、学科名、大学名
・キャッチコピー
・写真
・KVRsの指定のマーク
を配置して、デザインを作っていただきたいと思います。データや詳細は添付ファイルをご確認ください。
高校生(男女とも)に興味を持ってもらえるようなポップな雰囲気で、緑や農林業を支えて地域づくりを目指すようなイメージのデザインを希望します。沢山ある大学、学部パンフレットに埋もれず、「自然、環境、地域」に関心を持つ高校生に中を開いてもらえるような表紙デザインをご提案いただけますよう、お願いします。

●予算イメージ
今回のコンペで募集する表紙+残りの7ページ(全8ページ)全体で15万円以内を想定しています。

●その他
最終締め切り日の翌日には、依頼する方を選定します。
迅速にご連絡、ご対応いただける方を優先致します。

当選予定の方とは、金額や納期について最終の確認をした上、
コンペの納品・当選手続、次いで、追加分の直接依頼をいたします。

ご不明な点がございましたら、お気軽にお問い合わせください。
どうぞよろしくお願いします。
記載項目
添付資料の「表紙作成にあたってのお願い」ファイルをご参照ください。
サイズ
B5
ページ数
片面
希望イメージ
シンプル 複雑
単色 カラフル
暗い 明るい
日常 高級
遊び心 厳粛
未来的 伝統的
女性的 男性的
希望する色
緑系、水色系、茶系、全体はアースカラー系で背景は白(紙の色)を希望します。
納品ファイル
• 高解像度JPG (.jpg)
• イラストレーター形式 (.ai)
補足説明
KVRsのアイコンが使用できるかについて、お問合せをいただきましたので、学内で確認致しました。
今回のアイコン使用は、情報目的の範疇として理解でき、またいくつかのアイコンを抜き出す場合も、一列に配置すれば問題ないようです。
当初の依頼通りアイコンを入れたデザインをご提案していただけますよう、お願い致します。
沢山の良いご提案をいただきましたので、参加報酬の件数を増やしました。
■ 選んだ理由

30名ほどの教員・現役学生に全てのデザインを見てもらい、投票をしてもらった結果、票が多く入ったデザインでしたので、選定しました。色のバランスや写真が目に飛び込んでくる印象やテイストが良かったと思います。

■ 提案者全員のお礼・コメント

この度は、私どもの依頼に沢山の素晴らしいご提案をいただき、本当にありがとうございました。こちらの要望に応える形で、あるいは、また違った視点からのアイディアやキャッチコピーを意欲的にご提案いただき、感謝申し上げます。
魅力的なご提案が多い中で1件に絞るのは大変心苦しいのですが、高校生をターゲットにしていることから、学生に人気のデザインを選定させていただきました。
今後の広報活動に際して、Tovirkaの活用という選択肢を周りに紹介していきたいと思いますので、今後ともどうぞよろしくお願いします。

```html
<!DOCTYPE html>
<html lang="ja">
<head>
<meta charset="utf-8">
<title>地域環境科学部 パンフレット表紙</title>
<link href="https://fonts.googleapis.com/css2?family=Noto+Sans+JP:wght@500;700;900&display=swap" rel="stylesheet">
<style>
  :root {
    --paper: #ffffff;
    --ink: #1f1f1f;
    --forest: #3f8a3a;
    --region: #b4543a;
    --landscape: #2e8f78;
    --engineering: #d9a72a;
    --kvr-red: #d23b3b;
    --kvr-orange: #e59a2a;
    --kvr-green: #4c9b46;
    --kvr-teal: #2a8fb5;
    --kvr-brown: #b07a2c;
    --kvr-olive: #6f9a35;
  }
  * { margin: 0; padding: 0; box-sizing: border-box; }
  html, body { width: 848px; height: 1200px; overflow: hidden; background: var(--paper); }
  body { font-family: "Noto Sans JP", sans-serif; color: var(--ink); }
  .cover { position: relative; width: 848px; height: 1200px; overflow: hidden; background: var(--paper); }
  .cover-art { position: absolute; inset: 0; }
  .dept-label {
    position: absolute; display: flex; align-items: center; gap: 10px;
    color: #fff; font-weight: 700; font-size: 30px; letter-spacing: 0.06em; height: 58px; padding: 0 18px;
  }
  .dept-label .badges { display: flex; gap: 5px; }
  .badge { width: 30px; height: 30px; display: block; }
  .forest { left: 0; top: 0; background: var(--forest); }
  .region { right: 0; top: 430px; width: 460px; background: var(--region); justify-content: flex-end; }
  .landscape { right: 0; top: 760px; width: 250px; background: var(--landscape); justify-content: flex-end; }
  .engineering { left: 0; bottom: 0; width: 500px; height: 70px; background: var(--engineering); }
  .university { position: absolute; left: 120px; top: 410px; display: flex; align-items: center; gap: 14px; }
  .university .mark { width: 18px; height: 18px; background: var(--ink); }
  .university .name { font-size: 34px; font-weight: 900; letter-spacing: 0.12em; }
  .university-en { position: absolute; left: 152px; top: 462px; font-size: 15px; font-weight: 500; letter-spacing: 0.04em; }
  .faculty { position: absolute; left: 110px; top: 540px; font-size: 64px; font-weight: 900; letter-spacing: 0.08em; }
  .catch { position: absolute; left: 110px; top: 650px; font-size: 26px; font-weight: 700; line-height: 1.6; letter-spacing: 0.04em; }
  .faculty-badges { position: absolute; left: 590px; top: 640px; display: flex; gap: 6px; }
</style>
</head>
<body>
<main class="cover">
  <svg class="cover-art" width="848" height="1200" viewBox="0 0 848 1200">
    <defs>
      <linearGradient id="forestWork" x1="0" y1="0" x2="1" y2="1">
        <stop offset="0" stop-color="#5a6b3c"/><stop offset="0.6" stop-color="#3e4a2c"/><stop offset="1" stop-color="#6e5a3c"/>
      </linearGradient>
      <linearGradient id="forestWalk" x1="0" y1="0" x2="1" y2="1">
        <stop offset="0" stop-color="#9cc264"/><stop offset="0.5" stop-color="#5f8f3a"/><stop offset="1" stop-color="#3d6b2e"/>
      </linearGradient>
      <linearGradient id="tractorField" x1="0" y1="0" x2="1" y2="1">
        <stop offset="0" stop-color="#a9bfae"/><stop offset="0.5" stop-color="#5f8aa3"/><stop offset="1" stop-color="#8a8a6a"/>
      </linearGradient>
      <linearGradient id="parkLawn" x1="0" y1="0" x2="0" y2="1">
        <stop offset="0" stop-color="#c9a98a"/><stop offset="0.45" stop-color="#6f8a4a"/><stop offset="1" stop-color="#7fa84a"/>
      </linearGradient>
    </defs>
    <polygon role="img" aria-label="森の斜面で作業する学生たちの写真" points="0,0 510,0 360,380 0,380" fill="url(#forestWork)"/>
    <polygon role="img" aria-label="緑の森の中で調査する学生の写真" points="524,0 848,0 848,430 354,430" fill="url(#forestWalk)"/>
    <polygon role="img" aria-label="トラクターに乗る学生たちの写真" points="0,850 586,850 448,1200 0,1200" fill="url(#tractorField)"/>
    <polygon role="img" aria-label="夕暮れの芝生広場と木々の写真" points="606,810 848,810 848,1200 462,1200" fill="url(#parkLawn)"/>
  </svg>

  <div class="dept-label forest">森林総合科学科
    <span class="badges"><i class="badge" style="background:var(--kvr-olive)"></i><i class="badge" style="background:var(--kvr-orange)"></i></span>
  </div>

  <div class="dept-label region">
    <span class="badges"><i class="badge" style="background:var(--kvr-orange)"></i><i class="badge" style="background:var(--kvr-green)"></i><i class="badge" style="background:var(--kvr-teal)"></i></span>
    地域創成科学科
  </div>

  <div class="university"><span class="mark"></span><span class="name">東都農林大学</span></div>
  <div class="university-en">Toto University of Agriculture</div>

  <h1 class="faculty">地域環境科学部</h1>
  <div class="faculty-badges">
    <i class="badge" style="background:var(--kvr-orange)"></i><i class="badge" style="background:var(--kvr-green)"></i><i class="badge" style="background:var(--kvr-olive)"></i><i class="badge" style="background:var(--kvr-teal)"></i>
  </div>
  <p class="catch">身のまわりの自然や<br>生活環境を支える仕組みは<br>どうなっているの？</p>

  <div class="dept-label landscape">造園科学科</div>

  <div class="dept-label engineering">生産環境工学科
    <span class="badges"><i class="badge" style="background:var(--kvr-brown)"></i><i class="badge" style="background:var(--kvr-red)"></i><i class="badge" style="background:var(--kvr-teal)"></i></span>
  </div>
</main>
</body>
</html>
```